Hearth Twisters Grand Opening 2-for-1 Sale Postcard Design

Who we are: Hearth Twisters will come to you. We roll your medical marijuana in the privacy and safety of your home. We roll your medicine for you.

We need a postcard design that meets NPDS RCTZ requirements for our Grand Opening 2-for-1 Sale. Please include some or all of our logo.
Looking for elegant, upscale design. Appeal to luxury buyers with more money than time.
Updates

2-for-1 offer good thru March 31, 2015.Please add a small recycle image to convey the fact that we recycle. Added Tuesday, December 8, 2015

Target Market(s)

Income $50K+, Age 35+, College education, Left politically, No kids or older kids

Industry/Entity Type

Health Service

Requirements
Must have
• Our logo
• Our contact number: (574) 218-3065
• NPDS Postcard/RCTZ comptability layout on back of card.
• 2-for-1 Offer good thru March 31st, 2016.
Nice to have
• 2-3 colors, white text on dark green background
Should not have
• Images of marijuana. Please limit marijuana images to our logo.

```html
<!DOCTYPE html>
<html lang="en">
<head>
<meta charset="utf-8">
<title>Hearth Twisters – 2 for 1 Postcard</title>
<link rel="stylesheet" href="https://fonts.googleapis.com/css2?family=Bree+Serif&family=Signika:wght@400&display=swap">
<style>
  :root {
    --green-dark: #1b6d1e;
    --green-deep: #1f5c1a;
    --green-bright: #5ee21b;
    --green-pale: #b9e59a;
    --orange: #f08a1e;
    --cream: #e9e5c8;
    --charcoal: #2b2b28;
    --white: #ffffff;
  }
  * { margin: 0; padding: 0; box-sizing: border-box; }
  html, body { width: 1200px; height: 466px; overflow: hidden; background: var(--white); }
  .postcard { position: relative; width: 1200px; height: 466px; font-family: "Bree Serif", serif; }

  /* Front */
  .front { position: absolute; left: 0; top: 0; width: 608px; height: 466px; overflow: hidden; }
  .stripe-field { position: absolute; left: 0; width: 608px; }
  .stripe-field--top {
    top: 0; height: 227px;
    background: linear-gradient(90deg, #cfe6b4 0%, #e3dfbf 25%, #b8d99a 50%, #e6d9b6 75%, #c6e3a8 100%);
  }
  .stripe-field--bottom {
    bottom: 0; height: 30px;
    background: linear-gradient(90deg, var(--green-bright) 0%, var(--orange) 30%, var(--charcoal) 50%, var(--orange) 70%, var(--green-bright) 100%);
  }
  .front-brand {
    position: absolute; left: 0; top: 112px; width: 608px;
    display: flex; justify-content: center; align-items: center; gap: 14px;
  }
  .brand-dot { width: 26px; height: 26px; border-radius: 50%; background: var(--green-dark); }
  .brand-name { font-size: 44px; color: var(--green-dark); line-height: 1; }

  .offer-band {
    position: absolute; left: 0; top: 227px; width: 608px; height: 209px;
    background: var(--green-dark); color: var(--cream); text-align: center;
  }
  .offer-date { position: absolute; top: 15px; width: 100%; font-size: 15px; }
  .offer-date sup { font-size: 8px; }
  .rule { position: absolute; left: 50%; transform: translateX(-50%); }
  .rule--orange-top { top: 43px; width: 320px; height: 3px; background: var(--orange); }
  .offer-headline { position: absolute; top: 56px; width: 100%; font-size: 62px; line-height: 1; letter-spacing: 2px; }
  .rule--pale { top: 126px; width: 304px; height: 1px; background: var(--green-pale); }
  .rule--orange-bottom { top: 131px; width: 338px; height: 3px; background: var(--orange); }
  .offer-cta { position: absolute; top: 142px; width: 100%; font-size: 17px; }
  .rule--bright { top: 167px; width: 196px; height: 1px; background: var(--green-bright); }
  .offer-phone { position: absolute; top: 179px; width: 100%; font-size: 18px; }

  /* Back */
  .back-brand {
    position: absolute; left: 648px; top: 78px;
    display: flex; align-items: center; gap: 10px;
  }
  .back-brand .brand-name { font-size: 30px; }
  .back-brand .brand-dot { width: 18px; height: 18px; }
  .recycle-note { position: absolute; left: 703px; top: 388px; width: 120px; text-align: center; }
  .recycle-symbol { display: block; margin: 0 auto; width: 44px; height: 44px; border-radius: 50%; background: var(--green-bright); }
  .recycle-label { margin-top: 8px; font-family: "Signika", sans-serif; font-size: 14px; color: var(--orange); }
  .address-panel { position: absolute; left: 0; top: 0; width: 1200px; height: 466px; pointer-events: none; }
</style>
</head>
<body>
<main class="postcard">
  <section class="front">
    <div class="stripe-field stripe-field--top" role="img" aria-label="Striped pattern in pale green, cream and grey"></div>
    <div class="front-brand">
      <span class="brand-dot"></span>
      <span class="brand-name">Hearth Twisters</span>
    </div>
    <div class="offer-band">
      <p class="offer-date">Offer until 31<sup>st</sup> of March 2016</p>
      <span class="rule rule--orange-top"></span>
      <h1 class="offer-headline">2 FOR 1</h1>
      <span class="rule rule--pale"></span>
      <span class="rule rule--orange-bottom"></span>
      <p class="offer-cta">Book today</p>
      <span class="rule rule--bright"></span>
      <p class="offer-phone">(574) 218-3065</p>
    </div>
    <div class="stripe-field stripe-field--bottom" role="img" aria-label="Striped pattern in bright green, orange and charcoal"></div>
  </section>

  <section class="back">
    <div class="back-brand">
      <span class="brand-dot"></span>
      <span class="brand-name">Hearth Twisters</span>
    </div>
    <div class="recycle-note">
      <span class="recycle-symbol" role="img" aria-label="Recycling symbol"></span>
      <p class="recycle-label">we recycle.</p>
    </div>
    <svg class="address-panel" width="1200" height="466" viewBox="0 0 1200 466" aria-hidden="true">
      <line x1="903" y1="21" x2="903" y2="388" stroke="#5ee21b" stroke-width="3"/>
      <rect x="1100" y="32" width="74" height="96" fill="none" stroke="#5ee21b" stroke-width="2"/>
      <g stroke="#5ee21b" stroke-width="2">
        <line x1="941" y1="240" x2="1182" y2="240"/>
        <line x1="941" y1="281" x2="1182" y2="281"/>
        <line x1="941" y1="320" x2="1182" y2="320"/>
        <line x1="941" y1="360" x2="1182" y2="360"/>
      </g>
    </svg>
  </section>
</main>
</body>
</html>
```